Business Card: RW Office Partners - Your tidy answer finder

Business Name: RW Office Partners
Website: www.rwofficepartners.com.au
Email: marisol@rwofficepartners.com.au
Mobile: 61 487 902 346
Facebook: @rwofficepartners
Instrgram: @rwofficepartners

Brading Colours:
HEX
#986474
#ddccd3
#7a8498
#c9d8e4
#000000
#ffffff

Tag Line: Your organised problem solver

Link to DRAFT website:
https://helpdeskhub.sitebuilderx.com/rw-office-partners

About Page from the website:
My name is Marisol Bramwell, and I would love to assist you to become more productive in your day to day and achieve your business and personal goals.
My mission is to give you time, time to work on the important tasks of your business or to be able to spend more time with your family. I will take on the tasks you don’t have time for, don’t know well or simply don’t like to do.
I have an extensive background in Administration, Tender Coordination, Document Control, WHS and Quality Management working primarily in the Construction, Mining and Corporate World.
I am passionate about being organised, having order and making things in your life (and mine) easier! I love to watch something unfold and grow into something amazing! I am known for being the go-to problem solver, the organiser of all things, producing high standards of work even under pressure. I’m also a confident communicator, and I understand that you’re busy running your business.

Target Market(s)

Small to Medium Business who require assistance in their business by a virtual assistant.

Industry/Entity Type

Virtual Assistant

Contact Information for Business Card

Mobile: 61 487 902 346

Font styles to use
Sans Serif

Colors
ffffff

Requirements
Must have
• Branding Colours as outlined.
Contact Details as outlined.
Logo as provided.
Proper contact details - mobile, facebook, instragm, website.
Simple, Elegant, very clean looking.
Should not have
• Note cute with pictures.
Not too girly as still want to market to construction companies.

```html
<!DOCTYPE html>
<html lang="en">
<head>
<meta charset="utf-8">
<title>RW Office Partners – Business Card</title>
<link href="https://fonts.googleapis.com/css2?family=Open+Sans:wght@300;700&display=swap" rel="stylesheet">
<style>
  :root {
    --mauve: #986474;
    --slate: #7a8498;
    --ink: #000000;
    --paper: #ffffff;
  }
  * { margin: 0; padding: 0; box-sizing: border-box; }
  html, body { width: 1200px; height: 734px; overflow: hidden; background: var(--paper); }
  .card {
    position: relative; width: 1200px; height: 734px;
    background: var(--paper);
    font-family: "Open Sans", Arial, sans-serif;
  }
  .name-band {
    position: absolute; left: 0; top: 86px; width: 1200px; height: 69px;
    display: flex; align-items: center;
  }
  .name-band .bar { height: 100%; background: var(--slate); }
  .name-band .bar-left { width: 83px; flex: none; }
  .name-band .bar-right { flex: 1; }
  .person-name {
    padding: 0 22px 0 26px;
    font-weight: 700; font-size: 50px; line-height: 1;
    letter-spacing: 0.5px; color: var(--mauve); white-space: nowrap;
  }
  .brand-name {
    position: absolute; left: 155px; top: 326px; width: 290px;
    font-weight: 700; font-size: 36px; line-height: 1.15;
    color: var(--mauve);
  }
  .divider {
    position: absolute; left: 470px; top: 290px;
    width: 3px; height: 154px; background: var(--slate);
  }
  .contact-list { position: absolute; left: 514px; top: 298px; list-style: none; }
  .contact-item {
    display: flex; align-items: center; height: 47px;
    font-weight: 300; font-size: 31px; color: var(--ink); white-space: nowrap;
  }
  .contact-item svg { width: 34px; height: 34px; margin-right: 16px; flex: none; }
  .social-band {
    position: absolute; left: 0; top: 580px; width: 1200px; height: 69px;
    background: var(--mauve);
    display: flex; align-items: center; justify-content: center; gap: 56px;
  }
  .social-item {
    display: flex; align-items: center;
    font-weight: 300; font-size: 31px; color: var(--paper);
  }
  .social-mark { flex: none; margin-right: 12px; background: var(--paper); }
  .social-mark.circle { width: 32px; height: 32px; border-radius: 50%; }
  .social-mark.square { width: 29px; height: 29px; border-radius: 6px; }
</style>
</head>
<body>
<main class="card">
  <header class="name-band">
    <span class="bar bar-left"></span>
    <h1 class="person-name">MARISOL BRAMWELL</h1>
    <span class="bar bar-right"></span>
  </header>

  <div class="brand-name">RW Office<br>Partners</div>

  <div class="divider"></div>

  <ul class="contact-list">
    <li class="contact-item">
      <svg viewBox="0 0 34 34" aria-hidden="true">
        <g fill="none" stroke="#986474" stroke-width="2">
          <circle cx="17" cy="17" r="15"/>
          <ellipse cx="17" cy="17" rx="7" ry="15"/>
          <line x1="2" y1="17" x2="32" y2="17"/>
          <path d="M5 9 H29 M5 25 H29"/>
        </g>
      </svg>
      www.rwofficepartners.com.au
    </li>
    <li class="contact-item">
      <svg viewBox="0 0 34 34" aria-hidden="true">
        <rect x="2" y="7" width="30" height="21" fill="#986474"/>
        <path d="M3 8 L17 20 L31 8 M3 27 L13 17 M31 27 L21 17" fill="none" stroke="#ffffff" stroke-width="2"/>
      </svg>
      marisol@rwofficepartners.com.au
    </li>
    <li class="contact-item">
      <svg viewBox="0 0 34 34" aria-hidden="true">
        <path fill="#986474" d="M7 2 C4 2 1 5 1 9 C2 21 13 32 25 33 C29 33 32 30 32 27 L32 25 L25 20 L21 24 C16 22 12 18 10 13 L14 9 L9 2 Z"/>
      </svg>
      61 487 902 346
    </li>
  </ul>

  <footer class="social-band">
    <span class="social-item"><span class="social-mark circle"></span>@rwofficepartners</span>
    <span class="social-item"><span class="social-mark square"></span>@rwofficepartners</span>
  </footer>
</main>
</body>
</html>
```